Glamour By Tavi

I am a makeup artist looking for professional looking double sided business card. I would like to create a logo and incorporate a set of eyes as the periods above the name "Tavi" on the card.

front of card: Logo "Glamour by Tavi" written across diagonal (bottom left to top right)

Back of card:
1) Professional makeup artist serving New York & New Jersey (or similar to this text)
2) 917-555-0148
3) glamourbytavi@mailcove.com

Industry/Entity Type

Business

```html
<!DOCTYPE html>
<html lang="en">
<head>
<meta charset="UTF-8">
<title>Glamour By Tavi — Business Card</title>
<link rel="stylesheet" href="https://fonts.googleapis.com/css2?family=Josefin+Sans:wght@100;300;400&display=swap">
<style>
  :root {
    --backdrop: #e6e3df;
    --card: #000000;
    --ink: #ffffff;
    --gold-dark: #5a4526;
    --gold: #b8955a;
    --gold-light: #f1dcae;
  }
  * { margin: 0; padding: 0; box-sizing: border-box; }
  html, body {
    width: 1000px;
    height: 1200px;
    overflow: hidden;
    background: var(--backdrop);
    font-family: "Josefin Sans", sans-serif;
    color: var(--ink);
  }
  .canvas { position: relative; width: 1000px; height: 1200px; }
  .card {
    position: absolute;
    width: 918px;
    height: 424px;
    background: var(--card);
    overflow: hidden;
  }
  .card::after {
    content: "";
    position: absolute;
    top: 0; right: 0;
    width: 8px; height: 100%;
    background: linear-gradient(180deg, var(--gold-dark), var(--gold-light) 35%, var(--gold) 65%, var(--gold-dark));
  }
  .card--front { left: 40px; top: 128px; }
  .card--back { left: 35px; top: 643px; }

  .front-title {
    position: absolute;
    left: 18px; top: 12px;
    font-weight: 100;
    font-size: 90px;
    letter-spacing: 2px;
    white-space: nowrap;
  }
  .front-name {
    position: absolute;
    left: 0; right: 8px; top: 222px;
    text-align: center;
    font-weight: 100;
    font-size: 100px;
    letter-spacing: 22px;
    padding-left: 22px;
  }

  .back-tagline {
    position: absolute;
    left: 0; right: 8px; top: 22px;
    text-align: center;
    font-weight: 400;
    font-size: 26px;
    letter-spacing: 0.5px;
  }
  .back-name {
    position: absolute;
    left: 0; right: 8px; top: 180px;
    text-align: center;
    font-weight: 100;
    font-size: 80px;
    letter-spacing: 18px;
    padding-left: 18px;
  }
  .contact {
    position: absolute;
    top: 356px;
    display: flex;
    align-items: center;
    gap: 22px;
    font-weight: 300;
    font-size: 28px;
  }
  .contact--phone { left: 24px; }
  .contact--email { right: 22px; top: 350px; }
  .contact-icon { width: 40px; height: 40px; flex: none; }
</style>
</head>
<body>
<main class="canvas">
  <section class="card card--front" aria-label="Card front">
    <h1 class="front-title">GLAMOUR BY</h1>
    <p class="front-name">TAVI</p>
  </section>

  <section class="card card--back" aria-label="Card back">
    <p class="back-tagline">Professional makeup artist serving New York &amp; New Jersey</p>
    <p class="back-name">TAVI</p>

    <div class="contact contact--phone">
      <svg class="contact-icon" viewBox="0 0 40 40" aria-hidden="true">
        <defs>
          <linearGradient id="goldRing" x1="0" y1="0" x2="1" y2="1">
            <stop offset="0" stop-color="#f1dcae"/>
            <stop offset="0.5" stop-color="#b8955a"/>
            <stop offset="1" stop-color="#5a4526"/>
          </linearGradient>
        </defs>
        <circle cx="20" cy="20" r="18" fill="none" stroke="url(#goldRing)" stroke-width="2.5"/>
        <path d="M14 11c1.5-1 3-.5 3.6.8l1.3 3c.4 1-.1 1.8-.9 2.4l-1 .7c.8 2.3 2.3 4 4.6 5.2l.8-1c.6-.8 1.5-1.1 2.4-.6l2.8 1.6c1.2.7 1.4 2.2.4 3.4-1.3 1.6-3.4 2.2-5.6 1.2-4.8-2.2-8.4-6.1-10-11-.7-2.2-.1-4.5 1.6-5.7z" fill="url(#goldRing)"/>
      </svg>
      <span>917-555-0148</span>
    </div>

    <div class="contact contact--email">
      <svg class="contact-icon" viewBox="0 0 40 40" aria-hidden="true">
        <circle cx="20" cy="20" r="18" fill="none" stroke="url(#goldRing)" stroke-width="2.5"/>
        <rect x="10" y="13" width="20" height="14" fill="none" stroke="url(#goldRing)" stroke-width="1.8"/>
        <path d="M10 13l10 8 10-8" fill="none" stroke="url(#goldRing)" stroke-width="1.8"/>
      </svg>
      <span>glamourbytavi@mailcove.com</span>
    </div>
  </section>
</main>
</body>
</html>
```